Business Card Design For Tidecrest Audio

Tidecrest Audio is a small pro-audio company providing rental and install services for professional sound reinforcement. Focus is gigs (any gigs) needing high quality audio; from corporate to chamber music to hard hitting rock.

Tidecrest Audio
Pro-audio for your gig ... goosebump good
Doran Pelley
doran@tidecrestaudio.example.com.au
0482 356 071

We need a business card design and an "drop-off"' larger card (eg. one third A4 size: 99mm wide x 210mm high) with more details.
Updates

Please note I've had limited internet access for last few days and for the next four.  The work so far looks great .. I'll provide some individual feedback on the designs now.  Great work, many thanks, love the creativity!

Doran

Industry/Entity Type

Business

```html
<!DOCTYPE html>
<html lang="en">
<head>
<meta charset="utf-8">
<title>Tidecrest Audio – Drop-off Card</title>
<link rel="stylesheet" href="https://fonts.googleapis.com/css2?family=Special+Elite&display=swap">
<style>
  :root {
    --ink: #111111;
    --salmon: #f08a7c;
    --orange: #f09a3a;
    --amber: #eaa63a;
    --lime: #c6d83e;
    --leaf: #9fd26e;
    --mint: #4fc38c;
    --teal: #17a68f;
    --deep-teal: #0e8885;
    --card-w: 1200px;
    --card-h: 2544px;
  }
  html, body {
    margin: 0;
    padding: 0;
    width: var(--card-w);
    height: var(--card-h);
    overflow: hidden;
    background: #ffffff;
  }
  .card {
    position: relative;
    width: var(--card-w);
    height: var(--card-h);
    overflow: hidden;
    color: var(--ink);
    font-family: "Special Elite", "Courier New", monospace;
    background:
      repeating-linear-gradient(-62deg,
        rgba(255,255,255,0.10) 0 6px,
        rgba(255,255,255,0) 6px 22px,
        rgba(0,0,0,0.04) 22px 30px,
        rgba(255,255,255,0) 30px 52px),
      linear-gradient(170deg,
        var(--salmon) 0%,
        var(--orange) 18%,
        var(--amber) 30%,
        var(--lime) 45%,
        var(--leaf) 56%,
        var(--mint) 70%,
        var(--teal) 86%,
        var(--deep-teal) 100%);
  }
  .brand-name {
    position: absolute;
    top: 150px;
    left: 0;
    width: 100%;
    margin: 0;
    text-align: center;
    font-weight: 400;
    font-size: 190px;
    line-height: 1.15;
    letter-spacing: 4px;
    color: var(--ink);
  }
  .tagline {
    position: absolute;
    top: 960px;
    left: 0;
    width: 100%;
    margin: 0;
    text-align: center;
    font-size: 116px;
    line-height: 1.08;
    letter-spacing: 2px;
  }
  .contact {
    position: absolute;
    left: 615px;
    top: 2010px;
    transform: translate(-50%, -50%) rotate(-42deg);
    text-align: center;
    white-space: nowrap;
  }
  .contact-name {
    display: block;
    font-size: 104px;
    line-height: 1.1;
  }
  .contact-email {
    display: block;
    font-size: 60px;
    line-height: 1.3;
  }
  .contact-phone {
    display: block;
    font-size: 94px;
    line-height: 1.1;
    letter-spacing: 4px;
  }
</style>
</head>
<body>
  <main class="card">
    <h1 class="brand-name">Tidecrest<br>Audio</h1>
    <p class="tagline">Pro-audio for<br>your gig...<br>goosebump good</p>
    <address class="contact" style="font-style: normal;">
      <span class="contact-name">Doran Pelley</span>
      <span class="contact-email">doran@tidecrestaudio.example.com.au</span>
      <span class="contact-phone">0482 356 071</span>
    </address>
  </main>
</body>
</html>
```